Mesh Banner Design for Business Premises

We require the design of a large mesh banner to be installed across the front fence of our warehouse. The banner should prominently feature our existing Trelborn logo and brand colours (yellow, white, and black) and be designed to be highly visible from the road.

The overall aesthetic should be strong, masculine, and industrial, reflecting the nature of the scaffolding and construction industry. The background should be predominantly black, with our branding incorporated in yellow and white for strong contrast and readability.

The banner should clearly communicate the full scope of services we provide, including:

Scaffold Design
Scaffold Engineering
Scaffold Installation / Erection
Scaffold Dismantling

It should also indicate the types of projects and clients we service, including:

Commercial
Industrial
Residential
Civil

The design should feel bold and professional, with a construction-oriented style that aligns with the scaffolding industry. It should be clean, impactful, and easy to read from a distance, ensuring passing traffic can quickly understand our services.

Where possible, subtle industrial or structural design elements (such as scaffold components, steel textures, or linework) may be incorporated into the background to reinforce the industry theme while keeping the layout uncluttered.

The final design will be produced as a large-format mesh banner for outdoor installation, so it should be created with this application and viewing distance in mind.

```html
<!DOCTYPE html>
<html lang="en">
<head>
<meta charset="utf-8">
<title>Trelborn Mesh Banner</title>
<link href="https://fonts.googleapis.com/css2?family=Bebas+Neue&family=Montserrat:wght@400;500&display=swap" rel="stylesheet">
<style>
  :root {
    --page-bg: #f4f4f4;
    --banner-black: #0b0b0b;
    --steel-dark: #1a1a1a;
    --steel-mid: #2b2b2b;
    --brand-yellow: #f2b31d;
    --brand-white: #ffffff;
    --badge-grey: #2a2a2a;
  }
  * { margin: 0; padding: 0; box-sizing: border-box; }
  html, body {
    width: 1129px; height: 1200px; overflow: hidden;
    background: var(--page-bg);
  }
  .banner {
    position: absolute; left: 43px; top: 427px;
    width: 1043px; height: 346px;
    background: var(--banner-black);
    box-shadow: 0 10px 18px rgba(0,0,0,0.35);
    overflow: hidden;
    font-family: "Bebas Neue", "Oswald", sans-serif;
  }
  .banner__texture {
    position: absolute; inset: 0;
    background: radial-gradient(ellipse at 55% 50%, var(--steel-mid) 0%, var(--steel-dark) 45%, var(--banner-black) 100%);
  }
  .brand-mark {
    position: absolute; left: 31px; top: 100px; width: 186px;
    display: flex; align-items: center; gap: 10px;
    color: var(--brand-yellow); font-size: 44px; line-height: 1;
  }
  .brand-mark__square { width: 16px; height: 16px; background: var(--brand-yellow); flex: none; }
  .contact-badge {
    position: absolute; background: var(--badge-grey);
    font-family: "Montserrat", sans-serif; color: var(--brand-white);
  }
  .contact-badge--large { left: 38px; top: 232px; width: 175px; height: 43px; padding: 6px 0 0 58px; }
  .contact-badge--small { left: 824px; top: 298px; width: 117px; height: 29px; padding: 5px 0 0 42px; }
  .contact-badge__name { display: block; font-size: 8px; letter-spacing: 3px; font-weight: 500; }
  .contact-badge__phone { display: block; font-size: 14px; font-weight: 400; margin-top: 2px; }
  .contact-badge--small .contact-badge__name { font-size: 5.5px; letter-spacing: 2px; }
  .contact-badge--small .contact-badge__phone { font-size: 9px; margin-top: 1px; }
  .contact-badge__dot {
    position: absolute; left: 14px; top: 10px; width: 26px; height: 24px; background: var(--brand-yellow);
  }
  .contact-badge--small .contact-badge__dot { left: 9px; top: 7px; width: 18px; height: 16px; }
  .headline {
    position: absolute; left: 269px; top: 22px;
    font-size: 66px; line-height: 0.98; font-weight: 400; letter-spacing: 0.3px;
  }
  .headline__accent { color: var(--brand-yellow); display: block; }
  .headline__main { color: var(--brand-white); display: block; }
  .service {
    position: absolute; display: flex; align-items: center;
  }
  .service__bullet {
    position: absolute; left: -16px; top: 21px; width: 6px; height: 6px; border-radius: 50%;
    background: var(--brand-yellow);
  }
  .service__icon {
    width: 48px; height: 48px; border-radius: 4px; background: var(--brand-yellow);
  }
  .service__label {
    position: absolute; top: 2px;
    color: var(--brand-white); font-size: 27px; line-height: 0.92; white-space: nowrap;
  }
  .services-col-1 .service__label { left: 63px; }
  .services-col-2 .service__label { left: 67px; }
  .divider {
    position: absolute; left: 795px; top: 28px; width: 2px; height: 292px; background: var(--brand-yellow);
  }
  .projects__title {
    position: absolute; left: 822px; top: 24px;
    color: var(--brand-yellow); font-size: 31px; line-height: 0.98;
  }
  .project {
    position: absolute; left: 824px; display: flex; align-items: center; gap: 21px;
    color: var(--brand-white); font-size: 29px; line-height: 1; letter-spacing: 1px;
  }
  .project__icon { width: 30px; height: 30px; border-radius: 3px; background: var(--brand-yellow); }
</style>
</head>
<body>
  <section class="banner">
    <div class="banner__texture" role="img" aria-label="Dark photo of steel scaffold frames and tubes"></div>

    <div class="brand-mark"><span class="brand-mark__square"></span>TRELBORN</div>

    <div class="contact-badge contact-badge--large">
      <span class="contact-badge__dot"></span>
      <span class="contact-badge__name">TRELBORN</span>
      <span class="contact-badge__phone">1300 7 RAISE</span>
    </div>

    <h1 class="headline">
      <span class="headline__accent">COMPLETE SCAFFOLDING</span>
      <span class="headline__main">SERVICES</span>
    </h1>

    <div class="services-col-1">
      <div class="service" style="left:267px; top:184px;">
        <span class="service__bullet"></span>
        <span class="service__icon" role="img" aria-label="Scaffold design blueprint icon"></span>
        <span class="service__label">SCAFFOLD<br>DESIGN</span>
      </div>
      <div class="service" style="left:267px; top:268px;">
        <span class="service__bullet"></span>
        <span class="service__icon" role="img" aria-label="Scaffold engineering icon"></span>
        <span class="service__label">SCAFFOLD<br>ENGINEERING</span>
      </div>
    </div>
    <div class="services-col-2">
      <div class="service" style="left:480px; top:184px;">
        <span class="service__bullet"></span>
        <span class="service__icon" role="img" aria-label="Scaffold installation icon"></span>
        <span class="service__label">SCAFFOLD<br>INSTALLATION / ERECTION</span>
      </div>
      <div class="service" style="left:480px; top:268px;">
        <span class="service__bullet"></span>
        <span class="service__icon" role="img" aria-label="Scaffold dismantling icon"></span>
        <span class="service__label">SCAFFOLD<br>DISMANTLING</span>
      </div>
    </div>

    <div class="divider"></div>

    <h2 class="projects__title">TYPES OF PROJECTS<br>WE SERVE</h2>
    <div class="project" style="top:119px;"><span class="project__icon" role="img" aria-label="Commercial building icon"></span>COMMERCIAL</div>
    <div class="project" style="top:163px;"><span class="project__icon" role="img" aria-label="Factory icon"></span>INDUSTRIAL</div>
    <div class="project" style="top:206px;"><span class="project__icon" role="img" aria-label="House icon"></span>RESIDENTIAL</div>
    <div class="project" style="top:250px;"><span class="project__icon" role="img" aria-label="Crane icon"></span>CIVIL</div>

    <div class="contact-badge contact-badge--small">
      <span class="contact-badge__dot"></span>
      <span class="contact-badge__name">TRELBORN</span>
      <span class="contact-badge__phone">1300 7 RAISE</span>
    </div>
  </section>
</body>
</html>
```